The Corvane Agency

We are a pr, social media and strategy agency specializing in the pet industry. We would like a new dynamic design of our existing website. We think it is currently outdated and looks too corporate. We would like it to look more consumer oriented as we primarily market pet products. We would like warm imagery involving pets and while pets are fun, this is still a business website and needs to maintain a professional look. We are hired by business owners and executives.
I would like some of our work featured on the home page.
Our primary service tabs are:
Public Relations
Social Media
Product Consulting
Most of the content will remain the same but we are open to suggestions!
Our current website can be found at www.corvanepetpr.example.
We are open to other colors than in our logo and on our current page.
This is a design only project and will not require programming. The selected designer will need to provide at least one interior page in addition to the home page.

Industry/Entity Type

Pet

Requirements
Should not have
• Cartoon type figures. Pet puns.

```html
<!DOCTYPE html>
<html lang="en">
<head>
<meta charset="utf-8">
<title>The Corvane Agency — Home</title>
<link rel="stylesheet" href="https://fonts.googleapis.com/css2?family=Questrial&family=Lobster&display=swap">
<style>
  :root {
    --grass-dark: #2f5a14;
    --grass-mid: #5f8e2a;
    --grass-light: #8db54a;
    --panel: #ffffff;
    --ink: #1d1d1d;
    --ink-soft: #333333;
    --nav-black: #0d0d0d;
    --nav-edge: #2a2a2a;
    --accent: #5a8a12;
    --accent-dark: #3f6a08;
    --heading-green: #4a7a0e;
    --footer: #4e6e1c;
    --footer-dark: #3a5512;
    --footer-text: #dfe8cc;
    --white: #ffffff;
  }
  * { box-sizing: border-box; margin: 0; padding: 0; }
  html, body { width: 1200px; height: 675px; overflow: hidden; }
  body {
    position: relative;
    font-family: "Questrial", "Century Gothic", sans-serif;
    color: var(--ink);
    background: var(--grass-mid);
  }
  .page-backdrop {
    position: absolute; inset: 0;
    background: radial-gradient(ellipse at 50% 40%, var(--grass-light) 0%, var(--grass-mid) 45%, var(--grass-dark) 100%);
  }
  .logo-tab {
    position: absolute; left: 493px; top: 51px; width: 212px; height: 70px;
    background: var(--nav-black);
    border-radius: 10px 10px 0 0;
    box-shadow: 0 0 0 2px #3a3a3a inset;
    display: flex; align-items: flex-start; justify-content: center;
    padding-top: 18px;
  }
  .logo-name { font-family: "Questrial", sans-serif; font-size: 23px; line-height: 28px; color: var(--white); }
  .site-panel {
    position: absolute; left: 170px; top: 114px; width: 860px; height: 468px;
    background: var(--panel);
    border-radius: 20px;
    box-shadow: 0 6px 18px rgba(0,0,0,.35);
    z-index: 1;
  }
  .site-footer {
    position: absolute; left: 170px; top: 570px; width: 860px; height: 69px;
    background: var(--footer);
    border-radius: 0 0 20px 20px;
    border: 2px solid #7da03a;
    border-top: none;
    box-shadow: 0 6px 14px rgba(0,0,0,.4);
    z-index: 0;
  }
  .ribbon { position: absolute; left: 125px; top: 136px; width: 948px; height: 64px; z-index: 3; }
  .main-nav {
    position: absolute; left: 208px; top: 149px; z-index: 4;
    display: flex; align-items: center;
  }
  .main-nav a {
    color: var(--white); text-decoration: none;
    font-size: 15px; letter-spacing: .2px;
    padding: 7px 13px; border-radius: 16px; line-height: 17px;
  }
  .main-nav a.is-active { background: var(--accent); }
  .hero {
    position: absolute; left: 186px; top: 193px; width: 829px; height: 239px; z-index: 2;
    border-radius: 0 0 20px 20px; overflow: hidden;
  }
  .hero-photo {
    position: absolute; inset: 0;
    background: linear-gradient(90deg, #5e8a2c 0%, #7aa33e 45%, #c9a27a 62%, #d9b48c 72%, #6f9a35 88%, #5a8628 100%);
  }
  .hero-title {
    position: absolute; left: 62px; top: 82px;
    font-family: "Lobster", cursive; font-weight: 400; font-size: 33px; line-height: 38px; color: var(--white);
    text-shadow: 1px 2px 3px rgba(0,0,0,.55);
  }
  .hero-dots { position: absolute; left: 62px; top: 127px; display: flex; gap: 5px; }
  .hero-dots span {
    width: 14px; height: 14px; border-radius: 50%;
    background: #2f4d0c; box-shadow: inset 0 1px 2px rgba(0,0,0,.6);
  }
  .hero-dots span.is-current { background: #7fb224; }
  .feature { position: absolute; top: 448px; z-index: 2; }
  .feature-photo { position: absolute; top: 0; width: 126px; height: 119px; border-radius: 6px; }
  .feature--about .feature-photo {
    left: 192px; background: linear-gradient(135deg, #f4efe9 0%, #b96a3c 45%, #9c9c9c 75%, #f4efe9 100%);
  }
  .feature--consulting .feature-photo {
    left: 630px; background: radial-gradient(ellipse at 50% 55%, #d9c9ae 0%, #efe9e0 55%, #ffffff 100%);
  }
  .feature-body { position: absolute; top: 0; }
  .feature--about .feature-body { left: 336px; width: 264px; }
  .feature--consulting .feature-body { left: 771px; width: 238px; }
  .feature-heading { font-weight: 400; font-size: 19px; color: var(--ink-soft); line-height: 24px; margin-bottom: 2px; white-space: nowrap; }
  .feature-heading em { font-style: normal; color: var(--heading-green); }
  .feature-text { font-size: 11.5px; line-height: 16px; color: var(--ink); }
  .btn-more {
    display: inline-block; margin-top: 9px;
    background: var(--accent); color: var(--white);
    font-size: 12.5px; line-height: 15px; padding: 4px 9px; border-radius: 12px;
    box-shadow: 0 0 0 1px var(--accent-dark);
  }
  .copyright { position: absolute; left: 21px; top: 32px; font-size: 12px; color: var(--footer-text); }
  .social { position: absolute; left: 263px; top: 33px; display: flex; gap: 8px; }
  .social span { width: 14px; height: 14px; border-radius: 50%; background: #2c3e10; }
  .signup {
    position: absolute; left: 520px; top: 20px; width: 326px; height: 38px;
    background: var(--footer-dark); border-radius: 5px;
    border: 1px solid #6a8c30;
    display: flex; align-items: center; padding: 0 4px 0 10px;
  }
  .signup-field { flex: 1; font-size: 13px; color: #b9c99a; }
  .signup-btn {
    width: 90px; height: 28px; border-radius: 4px;
    background: linear-gradient(#4f7a16, #3c6210);
    border: 1px solid #79a034;
    color: #d8e6c0; font-size: 12.5px;
    display: flex; align-items: center; justify-content: center;
  }
</style>
</head>
<body>
  <div class="page-backdrop" role="img" aria-label="Soft-focus green lawn filling the page background"></div>

  <div class="logo-tab"><span class="logo-name">corvanepetpr</span></div>

  <div class="site-footer">
    <p class="copyright">Copyright@2013, All rights are reserved.</p>
    <div class="social" aria-label="Social links"><span></span><span></span></div>
    <div class="signup">
      <span class="signup-field">Your Email Id</span>
      <span class="signup-btn">Sign me up!</span>
    </div>
  </div>

  <div class="site-panel"></div>

  <svg class="ribbon" viewBox="0 0 948 64" aria-hidden="true">
    <polygon points="0,8 48,8 48,64 10,64 20,36" fill="#1a1a1a"/>
    <polygon points="948,8 900,8 900,64 938,64 928,36" fill="#1a1a1a"/>
    <rect x="30" y="0" width="888" height="60" fill="var(--nav-black)"/>
    <rect x="30" y="0" width="888" height="2" fill="var(--nav-edge)"/>
    <rect x="30" y="58" width="888" height="2" fill="#1f1f1f"/>
  </svg>

  <nav class="main-nav">
    <a class="is-active" href="#">HOME</a>
    <a href="#">ABOUT US</a>
    <a href="#">PUBLIC RELATIONS</a>
    <a href="#">SOCIAL MEDIA</a>
    <a href="#">PRODUCT CONSULTING</a>
    <a href="#">CONTACTS</a>
  </nav>

  <section class="hero">
    <div class="hero-photo" role="img" aria-label="Golden retriever puppy sitting on a green lawn"></div>
    <h1 class="hero-title">Welcome to our site</h1>
    <div class="hero-dots"><span class="is-current"></span><span></span><span></span></div>
  </section>

  <section class="feature feature--about">
    <div class="feature-photo" role="img" aria-label="Woman kneeling with two large brown dogs"></div>
    <div class="feature-body">
      <h2 class="feature-heading"><em>About</em> Us</h2>
      <p class="feature-text">Lorem ipsum dolor sit amet, consectetur adipisicing elit, sed do eiusmod tempor do ut labore et dolore magna do eiusmod.</p>
      <span class="btn-more">Get More</span>
    </div>
  </section>

  <section class="feature feature--consulting">
    <div class="feature-photo" role="img" aria-label="Fawn pug sitting on a white background"></div>
    <div class="feature-body">
      <h2 class="feature-heading"><em>Product</em> Consulting</h2>
      <p class="feature-text">Lorem ipsum dolor sit amet, consectetur adipisicing elit, sed do eiusmod tempor incididunt ut labore et dolore magna.</p>
      <span class="btn-more">Get More</span>
    </div>
  </section>
</body>
</html>
```